BRIMLOW Pizza and Wraps

We need a website for a new restaurant called BRIMLOW "PIZZA AND WRAPS".
I have attached fonts, background images, logo, images, content etc.
can provide you with what you need to get the website design done fast and easy

I have uploaded more images of the venue and some menu items. let me know if there is anything I need to provide to make your mission clear and easy

Reason: i would like a little time to provide more feedback to designers

Industry/Entity Type

Restaurant

Coding

Coded - Design and coding required

Number of Pages Required

5+ page

Colors

Designer to choose colors to be used in the design.

Requirements
Must have
• PAGES:
• Our Story
• Menu
• Reservations
• Catering & Delivery
• Contact

```html
<!DOCTYPE html>
<html lang="en">
<head>
<meta charset="UTF-8">
<title>Catering &amp; Event — Brimlow Pizza and Wraps</title>
<link rel="stylesheet" href="https://fonts.googleapis.com/css2?family=Raleway:wght@400;700&display=swap">
<style>
  :root {
    --page-bg: #e9eaee;
    --card-bg: #ffffff;
    --accent-blue: #c4d7f2;
    --accent-red: #ef534c;
    --heading: #2f323a;
    --body-text: #3d3f47;
  }
  * { margin: 0; padding: 0; box-sizing: border-box; }
  html, body {
    width: 1200px;
    height: 608px;
    overflow: hidden;
    background: var(--page-bg);
    font-family: "Raleway", sans-serif;
  }
  .catering-section {
    position: relative;
    width: 1200px;
    height: 608px;
    overflow: hidden;
  }
  .decor-shapes {
    position: absolute;
    inset: 0;
  }
  .info-card {
    position: absolute;
    left: 320px;
    top: 17px;
    width: 561px;
    height: 575px;
    background: var(--card-bg);
    text-align: center;
  }
  .card-title {
    position: absolute;
    top: 44px;
    left: 0;
    width: 100%;
    font-size: 47px;
    font-weight: 700;
    line-height: 56px;
    color: var(--heading);
    letter-spacing: 0.2px;
  }
  .card-copy {
    position: absolute;
    top: 116px;
    left: 0;
    width: 100%;
    font-size: 16px;
    line-height: 27px;
    color: var(--body-text);
  }
  .card-copy p + p { margin-top: 27px; }
  .card-copy .spacer-dot { margin-top: 0; }
  .request-button {
    position: absolute;
    left: 177px;
    top: 486px;
    width: 206px;
    height: 44px;
    border: 2px solid var(--accent-red);
    border-radius: 3px;
    background: transparent;
    color: var(--accent-red);
    font-family: "Raleway", sans-serif;
    font-size: 13px;
    line-height: 40px;
    text-decoration: none;
    display: block;
  }
</style>
</head>
<body>
  <section class="catering-section">
    <svg class="decor-shapes" width="1200" height="608" viewBox="0 0 1200 608" aria-hidden="true">
      <circle cx="845" cy="299" r="198" fill="var(--accent-blue)"/>
      <polygon points="150,548 330,368 330,548" fill="var(--accent-red)"/>
    </svg>

    <article class="info-card">
      <h1 class="card-title">CATERING &amp; EVENT</h1>
      <div class="card-copy">
        <p>A special event requires a unique experience.<br>Brimlow comes to You!</p>
        <p>Do you have to organize lunches or dinners,<br>business events or private parties?<br>Brimlow will recreate a Mediterranean atmosphere in<br>your home or wherever you prefer.</p>
        <p>Let Brimlow cater for your next event and make it<br>unforgettable. Create your own unique environment and<br>atmosphere to enjoy our selection of premium quality<br>food and beverages.</p>
        <p class="spacer-dot">.</p>
      </div>
      <a class="request-button" href="#request">Send Your Request</a>
    </article>
  </section>
</body>
</html>
```